Hawaii Real Estate Resort Report; Direct mail design template

Aloha designers!
Full color Bi-fold design template for a monthly or quarterly Hawaii real estate publication titled "The Tidewater Ledger". Design needs to be visually appealing and able to utilize various photos, text sections, graphs or charts, etc. For the Mava Reni Resort area on the southwest side of Oahu.
Needs to have a blank/clear area on the outside for mailing purposes and to adhere with QMSX requirements. (http://dox.qmsx-mailrules.example/fsm/documents/tech_guides/FSMReference.pdf)
Final design needs to be in an Adobe Illustrator (.ai) format per the attached Zelbrint.com templates. Bleed areas provided in the templates need to be adhered to so that we have a print-ready template with the necessary bleed areas.
All text areas need to be able to be edited and should not have outlined fonts unless it is text that will never be changed (ie: the title "The Tidewater Ledger"). Final design should incorporate appealing fonts and colors so that various text can be entered in and text size adjusted as needed.
The design template should incorporate a similar look and feel (color scheme) as the attached two-sided marketing info flyer on our vacation rental management services.
We can provide images, logos and other design components as needed.
Content helps:
- The Tidewater Ledger
- Specializing in Resort Real Estate & Vacation Rentals
- Volume 1, Issue 1
- Sections: Main body message section for welcome note/letter, sort of like an Editor's note. Resort Real Estate Sales From DATE to DATE (list or chart), Shore Lofts at Mava Reni Sales Update, Text areas for updates on some of the six resort communities, Photo of the month, Local Business Spotlight, Fun Facts section in sidebar (small area). Contact information with photo, name, phone, email, website.
Mahalo!
Just let me know if there are specific images or other content details that you require to create an initial design template. Thanks.

```html
<!DOCTYPE html>
<html lang="en">
<head>
<meta charset="utf-8">
<title>The Tidewater Ledger – Newsletter Template</title>
<link href="https://fonts.googleapis.com/css2?family=Barlow:wght@400;500;600&family=Arimo:wght@400;700&display=swap" rel="stylesheet">
<style>
:root{
  --backdrop:#232323;
  --paper:#ffffff;
  --red:#b41f3a;
  --tan:#c8b07a;
  --ink:#1a1a1a;
  --night:#0e0e0e;
  --gold:#e0c26a;
  --sea:linear-gradient(180deg,#7fb7e4 0%,#cfe3f1 30%,#b9a57a 55%,#5b8f4a 75%,#d9c9a0 100%);
}
*{box-sizing:border-box;margin:0;padding:0}
html,body{width:1200px;height:765px;overflow:hidden;background:var(--backdrop)}
.stage{position:absolute;left:0;top:0;width:1100px;height:701px;transform:scale(1.0909);transform-origin:0 0;font-family:"Arimo",Arial,sans-serif;color:var(--ink)}
.page{position:absolute;top:18px;width:521px;height:667px;background:var(--paper);overflow:hidden}
.page--front{left:18px}
.page--inside{left:562px}
.abs{position:absolute}
.body-copy{font-size:7.4px;line-height:1.32}
.body-copy p{margin-bottom:8px}

/* front */
.brand{left:0;top:0;width:330px;height:56px;padding:16px 0 0 24px}
.brand__name{font-family:"Barlow",sans-serif;font-weight:600;font-size:19px;color:var(--red);letter-spacing:.3px;display:flex;align-items:center;gap:8px}
.brand__dot{width:22px;height:22px;border-radius:50%;background:var(--tan)}
.brand__tag{font-size:6px;color:#2b5a8c;margin:2px 0 0 30px}
.callbox{left:330px;top:0;width:191px;height:56px;background:var(--red);padding:7px 0 0 10px;color:var(--gold)}
.callbox__label{font-family:"Barlow",sans-serif;font-size:10px}
.callbox__phone{font-family:"Barlow",sans-serif;font-size:25px;line-height:1}
.hero{left:0;top:56px;width:521px;height:208px;background:var(--sea)}
.titlebar{left:0;top:204px;width:312px;height:60px;background:var(--red);border-top:3px solid #fff;border-right:3px solid #fff;color:#fff;font-family:"Barlow",sans-serif;font-weight:500;font-size:29px;line-height:1;padding:15px 0 0 10px;white-space:nowrap;overflow:hidden}
.issue{left:316px;top:204px;width:72px;height:60px;background:var(--tan);border:3px solid #fff;color:var(--red);font-family:"Barlow",sans-serif;font-size:18px;line-height:1.05;padding:7px 0 0 6px}
.welcome{left:0;top:264px;width:315px;height:298px;padding:6px 14px}
.welcome h2{font-family:"Barlow",sans-serif;font-weight:500;font-size:24px;color:var(--red);margin-bottom:7px}
.signoff{font-size:7px;margin-top:4px}
.signature{width:90px;height:22px;margin:3px 0 3px 20px;background:linear-gradient(90deg,#e8e8e8,#f6f6f6)}
.sales{left:315px;top:264px;width:206px;height:298px;background:var(--red);padding:14px 16px}
.sales h3{font-family:"Barlow",sans-serif;font-weight:500;font-size:19px;color:var(--gold);text-align:center}
.pie{display:block;margin:12px auto 8px}
.legend{list-style:none;font-family:"Barlow",sans-serif;font-weight:600;font-size:10px;color:#fff}
.legend li{display:flex;align-items:center;gap:5px;line-height:1.25}
.tri{width:0;height:0;border-top:4px solid transparent;border-bottom:4px solid transparent;border-left:6px solid}
.contact{left:0;top:562px;width:521px;height:105px;background:var(--night);color:#fff}
.contact__cta{position:absolute;left:96px;top:6px;font-family:"Barlow",sans-serif;font-weight:600;font-size:10.5px;white-space:nowrap}
.portrait{position:absolute;background:linear-gradient(160deg,#6d8aa8,#c9a88c);border:2px solid var(--red)}
.agent{position:absolute;font-size:6px;line-height:1.35;color:#ddd}
.agent__name{font-family:"Barlow",sans-serif;font-weight:600;color:var(--gold);font-size:11px;line-height:1.15}
.agent__role{color:var(--gold);font-size:7px}
.badge{position:absolute;background:#444;border:1px solid #888}
.brandmark{position:absolute;font-family:"Barlow",sans-serif;font-weight:600;color:#fff}
.bio{position:absolute;left:276px;top:26px;width:238px;font-size:6.3px;line-height:1.4;text-align:right;color:#eee}
.bio strong{color:var(--gold);font-weight:700}

/* inside */
.market-head{left:0;top:0;width:338px;height:64px;background:var(--tan);padding:4px 0 0 12px}
.market-head h2{font-family:"Barlow",sans-serif;font-weight:500;font-size:31px;color:var(--red);line-height:1.05}
.market-head p{font-family:"Barlow",sans-serif;font-size:15px;color:var(--red)}
.market-cols{left:12px;top:70px;width:322px;display:grid;grid-template-columns:1fr 1fr;gap:10px;font-size:7.1px}
.market-cols h4{font-family:"Barlow",sans-serif;font-weight:600;color:var(--red);font-size:10px;margin:-2px 0 2px}
.inside-contact{left:0;top:267px;width:335px;height:62px;background:var(--night);color:#fff}
.inside-contact__cta{position:absolute;left:6px;top:2px;font-family:"Barlow",sans-serif;font-weight:600;font-size:9px;white-space:nowrap}
.mail-lines{left:70px;top:412px;width:200px}
.mail-lines span{display:block;height:1px;background:#333;margin-bottom:24px}
.stamp{left:18px;top:574px;width:34px;height:48px;border:1px solid #333}
.side{left:341px;width:180px}
.photo-month{top:0;height:182px;background:var(--red);padding:6px 10px}
.side h3{font-family:"Barlow",sans-serif;font-weight:500;font-size:17px;color:var(--gold)}
.photo-month__img{width:160px;height:95px;margin:8px 0 4px;background:linear-gradient(180deg,#76aee0,#5f9c62 60%,#3c8fb2)}
.side-note{font-size:5.8px;line-height:1.35;color:#fff}
.spotlight{top:187px;height:145px;background:var(--tan);padding:6px 10px;border:3px solid #fff;border-left:none;border-right:none}
.spotlight h3{color:#fff}
.spotlight__img{float:right;width:56px;height:56px;margin:4px 0 2px 4px;background:linear-gradient(180deg,#5d89b5,#c79a63)}
.flipside{top:337px;height:330px;background:var(--red);color:#fff}
.flipside__inner{position:absolute;inset:0;transform:rotate(180deg);padding:14px 12px}
.flip-mark{position:absolute;left:70px;top:235px;width:40px;height:40px;border-radius:50%;border:2px solid var(--tan)}
.flip-name{position:absolute;left:0;right:0;top:128px;text-align:center;font-family:"Barlow",sans-serif;font-weight:600;font-size:20px}
.flip-name--second{top:74px}
</style>
</head>
<body>
<div class="stage">

  <!-- Front cover -->
  <section class="page page--front">
    <div class="abs brand">
      <div class="brand__name"><span class="brand__dot"></span>IslandNestFinder.com</div>
      <div class="brand__tag">Real Estate &amp; Vacation Rentals by Kellan Asheford &amp; Associates</div>
    </div>
    <div class="abs callbox">
      <div class="callbox__label">Call us</div>
      <div class="callbox__phone">(808) 555-0142</div>
    </div>
    <div class="abs hero" role="img" aria-label="Photo of a beachfront resort with palm trees, a sandy lagoon and mountains"></div>
    <h1 class="abs titlebar">The Tidewater Ledger</h1>
    <div class="abs issue">Vol. 1<br>Issue 1</div>

    <article class="abs welcome">
      <h2>Welcome Note</h2>
      <div class="body-copy">
        <p>Lorem ipsum dolor sit amet, consectetur adipisicing elit, sed do eiusmod tempor incididunt ut labore et dolore magna aliqua. Ut enim ad minim veniam, quis nostrud exercitation ullamco laboris nisi ut aliquip ex ea commodo consequat. Duis aute irure dolor in reprehenderit in voluptate velit esse cillum dolore eu fugiat nulla pariatur. Excepteur sint occaecat cupidatat non proident, sunt in culpa qui officia deserunt mollit anim id est laborum</p>
        <p>Sed ut perspiciatis unde omnis iste natus error sit voluptatem accusantium doloremque laudantium, totam rem aperiam, eaque ipsa quae ab illo inventore veritatis et quasi architecto beatae vitae dicta sunt explicabo.</p>
        <p>Nemo enim ipsam voluptatem quia voluptas sit aspernatur aut odit aut fugit, sed quia consequuntur magni dolores eos qui ratione voluptatem sequi nesciunt. Neque porro quisquam est, qui dolorem ipsum quia dolor sit amet, consectetur, adipisci velit, sed quia non numquam eius modi tempora incidunt ut labore et dolore magnam aliquam quaerat voluptatem.</p>
        <p>Ut enim ad minima veniam, quis nostrum exercitationem ullam corporis suscipit laboriosam, nisi ut aliquid ex ea commodi consequatur? Quis autem vel eum iure reprehenderit qui in ea voluptate velit esse quam nihil molestiae consequatur, vel illum qui dolorem eum fugiat quo voluptas nulla pariatur</p>
      </div>
      <div class="signoff">Mahalo</div>
      <div class="signature" role="img" aria-label="Handwritten signature"></div>
      <div class="signoff">Kellan Asheford</div>
    </article>

    <aside class="abs sales">
      <h3>2014 Sales to Date</h3>
      <svg class="pie" width="130" height="110" viewBox="-65 -55 130 110" aria-label="Pie chart of sales by community">
        <path d="M0 5 L0 -45 A50 40 0 0 1 50 5 Z" fill="#62c04a"/>
        <path d="M0 5 L50 5 A50 40 0 0 1 20 42 Z" fill="#f0c22e"/>
        <path d="M0 5 L20 42 A50 40 0 0 1 -25 40 Z" fill="#f28a2a"/>
        <path d="M0 5 L-25 40 A50 40 0 0 1 -50 8 Z" fill="#e2333c"/>
        <path d="M0 5 L-50 8 A50 40 0 0 1 -38 -22 Z" fill="#d85fa8"/>
        <path d="M0 5 L-38 -22 A50 40 0 0 1 0 -45 Z" fill="#8a5cc9"/>
      </svg>
      <ul class="legend">
        <li><span class="tri" style="color:#62c04a"></span>Shore Lofts</li>
        <li><span class="tri" style="color:#6a72d8"></span>Nalu Vista</li>
        <li><span class="tri" style="color:#d85fa8"></span>Palm Grove Plantation :</li>
        <li><span class="tri" style="color:#e2333c"></span>Mava Reni Kai Golf Estates</li>
        <li><span class="tri" style="color:#f28a2a"></span>Fairways :</li>
        <li><span class="tri" style="color:#f0c22e"></span>Hillside :</li>
      </ul>
    </aside>

    <footer class="abs contact">
      <div class="contact__cta">Contact Kellan today for a FREE no obligation market analysis of your property</div>
      <div class="portrait" style="left:20px;top:9px;width:66px;height:80px" role="img" aria-label="Agent portrait photo"></div>
      <div class="agent" style="left:96px;top:24px">
        <div class="agent__name">Kellan Asheford</div>
        <div class="agent__role">RA, MBA, Property Manager</div>
        1780 Lumaho Ave., Suite #204<br>Honolulu, HI 96799<br>Mobile: 808-555-0142<br>Fax: 808-555-0187<br>Kellan@IslandNestFinder.com<br>www.IslandNestFinder.com<br><span style="color:var(--red)">License: RS-51820</span>
      </div>
      <div class="badge" style="left:198px;top:30px;width:58px;height:22px"></div>
      <div class="brandmark" style="left:198px;top:60px;font-size:12px">Coralline</div>
      <div class="bio"><strong>Your Local Agent Specializing in Resort Real Estate &amp; Vacation Rentals</strong><br>Kellan's family has owned multiple Mava Reni properties since 2008 and he resides full-time in Mava Reni Kai Golf Estates &amp; Villas. His team actively manages various Mava Reni vacation rental properties and he has been involved with the sale of more than $15 million of Mava Reni real estate in 2014 alone. His friendly personality and tech-savvy marketing approach have enabled him to deliver consistent results for his clients.</div>
    </footer>
  </section>

  <!-- Inside / mailing panel -->
  <section class="page page--inside">
    <header class="abs market-head">
      <h2>How’s The Market?</h2>
      <p>Market updates, info</p>
    </header>
    <div class="abs market-cols">
      <div>
        <p>Lorem ipsum dolor sit amet, consectetur adipisicing elit, sed do eiusmod tempor incididunt ut labore et dolore magna aliqua. Ut enim ad minim veniam, quis nostrud exercitation ullamco laboris nisi ut aliquip ex ea commodo consequat. Duis aute irure dolor in reprehenderit in voluptate velit esse cillum dolore eu fugiat nulla pariatur. Excepteur sint occaecat cupidatat non proident, sunt in culpa qui officia deserunt mollit anim id est laborum</p><br>
        <h4>consectetur adipisicing</h4>
        <p>Sed ut perspiciatis unde omnis iste natus error sit voluptatem accusantium doloremque laudantium, totam rem aperiam, eaque ipsa quae ab illo inventore veritatis et quasi architecto beatae vitae dicta sunt explicabo.</p><br>
        <p>Nemo enim ipsam voluptatem quia voluptas sit aspernatur aut odit aut fugit, sed quia conse-</p>
      </div>
      <div>
        <p>quuntur magni dolores eos qui ratione voluptatem sequi nesciunt. Neque porro quisquam est, qui dolorem ipsum quia dolor sit amet, consectetur, adipisci velit, sed quia non numquam eius modi tempora incidunt ut labore et dolore magnam aliquam quaerat voluptatem.</p><br>
        <h4>consectetur adipisicing</h4>
        <p>Ut enim ad minima veniam, quis nostrum exercitationem ullam corporis suscipit laboriosam, nisi ut aliquid ex ea commodi consequatur? Quis autem vel eum iure reprehenderit qui in ea voluptate velit esse quam nihil molestiae consequatur, vel illum qui dolorem eum fugiat quo voluptas nulla pariatur</p><br>
        <p>Ut enim ad minima veniam, quis nostrum exercitationem ullam corporis suscipit laboriosam, nisi ut aliquid ex ea commodi consequatur? Quis autem vel eum iure reprehenderit qui</p>
      </div>
    </div>

    <div class="abs inside-contact">
      <div class="inside-contact__cta">Contact Kellan today for a FREE no obligation market analysis of your property</div>
      <div class="portrait" style="left:8px;top:16px;width:38px;height:42px" role="img" aria-label="Agent portrait photo"></div>
      <div class="agent" style="left:56px;top:14px;font-size:5px">
        <div class="agent__name" style="font-size:10px">Kellan Asheford</div>
        <div class="agent__role" style="font-size:6px">RA, MBA, Property Manager</div>
        <div class="agent__role" style="font-size:6px">Coralline Pacific Properties, LLC</div>
        <span style="color:var(--red)">License: RS-51820</span>
      </div>
      <div class="agent" style="left:148px;top:14px;font-size:5px">1780 Lumaho Ave., Suite #204<br>Honolulu, HI 96799<br>Mobile: 808-555-0142<br>Fax: 808-555-0187<br>Kellan@IslandNestFinder.com<br>www.IslandNestFinder.com</div>
      <div class="badge" style="left:242px;top:20px;width:84px;height:30px"></div>
    </div>

    <div class="abs mail-lines"><span></span><span></span><span></span><span></span><span></span></div>
    <div class="abs stamp"></div>

    <aside class="abs side photo-month">
      <h3>Photo of the Month</h3>
      <div class="photo-month__img" role="img" aria-label="Photo of a resort lagoon pool with palm trees and a gazebo"></div>
      <p class="side-note">Lorem ipsum dolor sit amet, consectetur adipisicing elit, sed do eiusmod tempor incididunt ut labore et dolore magna aliqua. Ut enim ad minim veniam, quis nostrud exercitation ullamco laboris nisi ut aliqu</p>
    </aside>
    <aside class="abs side spotlight">
      <h3>Business Spotlight</h3>
      <div class="spotlight__img" role="img" aria-label="Photo of an oceanfront restaurant table"></div>
      <p class="side-note">Lorem ipsum dolor sit amet, consectetur adipisicing elit, sed do eiusmod tempor incididunt ut labore et dolore magna aliqua. Ut enim ad minim veniam, quis nostrud exercitation ullamco laboris nisi ut aliquip ex ea commodo consequat. Duis aute irure dolor in reprehenderit in voluptate velit esse cillum dolore eu fugiat nulla pariatur. Excepteur sint occaecat cupidatat non proident, sunt in culpa qui officia deserunt mollit anim id est laborum</p>
    </aside>
    <aside class="abs side flipside">
      <div class="flipside__inner">
        <p class="side-note">Lorem ipsum dolor sit amet, consectetur adipisicing elit, sed do eiusmod tempor incididunt ut labore et dolore magna aliqua. Ut enim ad minim veniam, quis nostrud exercitation ullamco laboris nisi ut aliquip ex ea commodo consequat. Duis aute irure dolor in reprehenderit in voluptate velit esse cillum dolore eu fugiat nulla pariatur. Excepteur sint occaecat cupidatat non proident, sunt in culpa qui officia deserunt mollit anim id est laborum</p>
        <div class="flip-name flip-name--second">Coralline</div>
        <div class="flip-name">Coralline</div>
        <div class="flip-mark"></div>
      </div>
    </aside>
  </section>

</div>
</body>
</html>
```